Tallow HVAC Services - High end letter head, Quote Template & Invoice Template

Provide word documents for the below.
- Letterhead for emails & letters.
- Quote template (similar to the attached)
- Invoice template (similar to the attached)
Logo colours should be used.
Modern, bold, professional look.
Tallow Logo - Veskor Specialist Dealer logo - Contact information

See attachments of previously used documents.

Target Market(s)

High end clients

Industry/Entity Type

Air Conditioning & Mechanical Ventilation (HVAC)

Font styles to use
Sans Serif
Other font styles liked:
• Arial Narrow or similar - Text similar to the TALLOW logo

Requirements
Must have
• Tallow Logo - Veskor Specialist Dealer logo - Contact information
Nice to have
• Logo colours used throughout the documents
Should not have
• Bright colours, yellow, pink, green etc

```html
<!DOCTYPE html>
<html lang="en">
<head>
<meta charset="utf-8">
<title>Tallow HVAC Services – Letterhead</title>
<link href="https://fonts.googleapis.com/css2?family=Archivo+Narrow:wght@400;700&family=Arimo:wght@400;700&family=Open+Sans:wght@400;600&display=swap" rel="stylesheet">
<style>
  :root {
    --backdrop: #d9d9d9;
    --paper: #f6f5f3;
    --header-black: #000000;
    --brand-red: #d7222a;
    --brand-blue: #1a5fb4;
    --badge-blue: #1c8fd8;
    --ink: #3a3a3a;
    --ink-soft: #555555;
    --footer-grey: #5c5c5c;
    --white: #ffffff;
  }
  * { box-sizing: border-box; margin: 0; padding: 0; }
  html, body { width: 912px; height: 1200px; overflow: hidden; }
  body { background: var(--backdrop); position: relative; font-family: "Arimo", Arial, sans-serif; }

  .letterhead {
    position: absolute; left: 95px; top: 92px; width: 722px; height: 1016px;
    background: var(--paper); overflow: hidden;
    box-shadow: 0 6px 22px rgba(0,0,0,.25);
  }

  .masthead {
    position: absolute; left: 0; top: 0; width: 100%; height: 113px;
    background: var(--header-black); color: var(--white);
  }
  .brand { position: absolute; left: 54px; top: 30px; }
  .brand-name-row { display: flex; align-items: center; gap: 8px; }
  .brand-square { width: 16px; height: 16px; background: var(--brand-red); }
  .brand-name {
    font-family: "Archivo Narrow", "Arial Narrow", sans-serif; font-weight: 700;
    font-size: 30px; line-height: 1; letter-spacing: .5px; color: var(--white);
  }
  .brand-sub {
    font-family: "Archivo Narrow", "Arial Narrow", sans-serif; font-weight: 700;
    font-size: 11px; color: var(--brand-red); margin-left: 60px; margin-top: 1px; letter-spacing: .3px;
  }
  .brand-tagline {
    font-family: "Archivo Narrow", "Arial Narrow", sans-serif;
    font-size: 9.5px; color: var(--white); letter-spacing: .6px; margin-top: 3px;
  }

  .contact-list { position: absolute; left: 482px; top: 34px; list-style: none; font-size: 14px; line-height: 18px; }
  .contact-list li { display: flex; align-items: center; gap: 7px; }
  .contact-list svg { width: 11px; height: 11px; fill: var(--badge-blue); flex: none; }

  .letter-body { position: absolute; left: 72px; top: 244px; width: 581px; color: var(--ink); }
  .salutation { font-size: 21px; color: var(--ink); margin-bottom: 30px; }
  .letter-body p.copy {
    font-size: 11.6px; line-height: 17px; text-align: justify; margin-bottom: 17px; color: var(--ink-soft);
  }
  .sign-off { position: absolute; left: 72px; top: 690px; font-size: 11.6px; color: var(--ink-soft); }
  .signature-area {
    position: absolute; left: 68px; top: 717px; width: 96px; height: 40px;
    background: linear-gradient(180deg, transparent 40%, rgba(20,20,30,.35) 50%, transparent 60%);
  }
  .signatory { position: absolute; left: 76px; top: 772px; }
  .signatory-name { font-size: 16px; color: var(--ink); }
  .signatory-role { font-size: 12.5px; color: var(--ink-soft); margin-top: 3px; }

  .dealer-badge { position: absolute; left: 520px; top: 874px; display: flex; align-items: center; gap: 6px; }
  .dealer-square { width: 20px; height: 20px; background: var(--badge-blue); }
  .dealer-name {
    font-family: "Arimo", Arial, sans-serif; font-weight: 700; font-size: 24px; color: var(--brand-blue); line-height: 1;
  }
  .dealer-caption {
    position: absolute; left: 582px; top: 900px; font-size: 6.5px; font-weight: 700;
    letter-spacing: .5px; color: var(--ink);
  }

  .footer-wave { position: absolute; left: 0; bottom: 0; width: 722px; height: 130px; }
  .footer-legal {
    position: absolute; left: 0; bottom: 8px; width: 100%; text-align: center;
    font-family: "Open Sans", Arial, sans-serif; font-size: 11px; color: var(--white);
  }
</style>
</head>
<body>
  <article class="letterhead">
    <header class="masthead">
      <div class="brand">
        <div class="brand-name-row">
          <span class="brand-square"></span>
          <span class="brand-name">TALLOW</span>
        </div>
        <div class="brand-sub">HVAC SERVICES PTY LTD.</div>
        <div class="brand-tagline">| HEATING | VENTILATION | AIR CONDITIONING |</div>
      </div>
      <ul class="contact-list">
        <li><svg viewBox="0 0 12 12"><path d="M2.5 0.5l2 2.3-1 1.4c.7 1.5 1.8 2.6 3.3 3.3l1.4-1 2.3 2-1.2 2.1C5 10.3 1.7 7 .4 1.7z"/></svg>0400 000 000</li>
        <li><svg viewBox="0 0 12 12"><path d="M0 2h12v1.2L6 7 0 3.2z M0 4.6l6 3.8 6-3.8V10H0z"/></svg>office@tallowhvac.example</li>
        <li><svg viewBox="0 0 12 12"><circle cx="6" cy="6" r="6"/></svg>www.tallowhvac.example</li>
      </ul>
    </header>

    <section class="letter-body">
      <h1 class="salutation" style="font-weight:400">Dear Mr. Harlow,</h1>
      <p class="copy">Lorem ipsum dolor sit amet, consectetur adipiscing elit. Donec orci purus, luctus vitae dignissim eu, iaculis sed purus. Vivamus faucibus, ipsum nec aliquet viverra, leo mauris condimentum ligula, sit amet sagittis enim ligula quis arcu. Nam egestas tortor id nisi porttitor mattis. In tortor ante, ultricies in suscipit a, tempus non massa. Vivamus et auctor mi. Fusce vel massa nulla. Phasellus nec eros mauris, et scelerisque orci.</p>
      <p class="copy">Donec malesuada orci vitae nulla accumsan porta a id massa. Quisque accumsan iaculis magna sit amet fringilla. Maecenas consequat, magna eget tincidunt semper, odio nibh rutrum mi, id feugiat ante nisi eu risus. Vestibulum nunc orci, rhoncus a placerat in, ultricies in mi. Cras mattis varius eros, vel fringilla nisi suscipit eget. Quisque scelerisque sagittis nulla at porttitor.</p>
      <p class="copy">Sed id augue vitae urna euismod commodo aliquet a quam. Pellentesque arcu velit, cursus et malesuada ut, consequat et diam. Nullam erat sem, rhoncus id ullamcorper vitae, rhoncus et arcu. In ultricies ultricies nulla, ut rutrum nisi iaculis at. Donec eu magna a metus ornare faucibus. Fusce aliquet faucibus ultricies. Morbi semper, est id tincidunt gravida, sem arcu adipiscing lacus, ac bibendum nulla leo eu purus. Quisque nec diam sed risus consectetur a ccumsan quis quis nibh. Vestibulum id purus lorem.</p>
      <p class="copy">It is a long established fact that a reader will be distracted by the readable content of a page when looking at its layout. The point of using Lorem Ipsum is that it has a more-or-less normal distribution of letters, as opposed to using 'Content here, content here', making it look like readable English. Many desktop publishing packages</p>
    </section>

    <p class="sign-off">Sincerely,</p>
    <div class="signature-area" role="img" aria-label="Handwritten signature of Peter Harlow"></div>
    <div class="signatory">
      <div class="signatory-name">Peter Harlow</div>
      <div class="signatory-role">CEO/ Founder</div>
    </div>

    <div class="dealer-badge">
      <span class="dealer-square"></span>
      <span class="dealer-name">VESKOR</span>
    </div>
    <div class="dealer-caption">SPECIALIST DEALER</div>

    <svg class="footer-wave" viewBox="0 0 722 130" preserveAspectRatio="none" aria-hidden="true">
      <path d="M0 40 C120 20 250 30 360 55 C470 78 600 50 722 0 L722 130 L0 130 Z" fill="var(--brand-blue)"/>
      <path d="M0 40 C120 20 250 30 360 55 L360 130 L0 130 Z" fill="var(--brand-red)"/>
      <path d="M0 52 C120 32 250 44 360 66 C470 86 600 60 722 12 L722 130 L0 130 Z" fill="var(--white)"/>
      <path d="M0 58 C120 38 250 52 360 72 C470 92 600 68 722 20 L722 130 L0 130 Z" fill="var(--footer-grey)"/>
    </svg>
    <footer class="footer-legal">ABN: 00 000 000 000 | Licence No: 000000X | ARC No: AU00000</footer>
  </article>
</body>
</html>
```